依頼詳細
残暑お見舞い申し上げます

コロナ禍と暑さで汗が噴き出るような日々が続きますが、いかがお過ごしでしょうか?
汗はかけばかくほど、老廃物が体内から出て、心も体も健康になります。
汗をかかないようにすることは、決して良いことではありません。
会社にとっても、今年は汗(特別損失)を出せるチャンスです。
個人も会社もたくさんの汗を出して、より健康体になられること、心より祈念申し上げます。

★写真に添える文章:松本清志の最新刊
「伸びる会社へ組み直す」
定価10,780円(税込み)
記載項目
ノルフェン・パートナーズ
松本 清志・長谷 宗一郎・柴田 昌平
希望イメージ
シンプル 複雑
単色 カラフル
暗い 明るい
日常 高級
遊び心 厳粛
未来的 伝統的
女性的 男性的
希望する色
水色系
納品ファイル
• 高解像度JPG (.jpg)
補足説明
■ 選んだ理由

今年はコロナのイベント中止で花火大会もなくなるなかで、
もってこいのデザインでした。
文字の並べ方に工夫が見られ、メッセージとバックのコントラストが素敵でした。
一目見ておしゃれで気に入りました。

■ 提案者全員のお礼・コメント

この度は、ご応募ありがとうございました。
毎回、新たなご提案が来るのが楽しみでした。素敵なご応募をありがとうございました。

```html
<!DOCTYPE html>
<html lang="ja">
<head>
<meta charset="UTF-8">
<title>残暑お見舞い申し上げます</title>
<link rel="stylesheet" href="https://fonts.googleapis.com/css2?family=Shippori+Mincho:wght@500;700&display=swap">
<style>
:root{
  --ink:#1f2a36;
  --sky-top:#ffffff;
  --sky-mid:#cfe4f6;
  --sky-deep:#6fa6d6;
  --city:#4f7fae;
  --city-dark:#2c4f78;
  --strip:#ffffff;
  --book:#8a1f24;
}
*{margin:0;padding:0;box-sizing:border-box}
html,body{width:809px;height:1200px;overflow:hidden;background:#fff}
.card{
  position:relative;width:809px;height:1200px;overflow:hidden;
  background:linear-gradient(180deg,var(--sky-top) 0%,var(--sky-top) 30%,var(--sky-mid) 55%,var(--sky-deep) 78%);
  font-family:"Shippori Mincho",serif;color:var(--ink);
}
.v{position:absolute;writing-mode:vertical-rl;white-space:nowrap}
.title{font-size:58px;font-weight:700;letter-spacing:4px;top:40px}
.title.first{left:680px}
.title.second{left:600px;top:72px}
.message{position:absolute;right:252px;top:70px;height:500px;writing-mode:vertical-rl;
  font-size:17px;line-height:26px;letter-spacing:1px;font-weight:500}
.message p{white-space:nowrap}
.company{left:290px;top:300px;font-size:18px;letter-spacing:2px;font-weight:500}
.name{font-size:18px;letter-spacing:3px;font-weight:500;top:330px}
.name.n1{left:250px}.name.n2{left:215px}.name.n3{left:180px}
.chart{position:absolute;left:0;top:0}
.city{position:absolute;left:0;top:860px;width:809px;height:280px;
  background:linear-gradient(180deg,rgba(255,255,255,0) 0%,var(--city) 40%,var(--city-dark) 100%)}
.book{position:absolute;left:690px;top:1018px;width:80px;height:116px;
  background:linear-gradient(135deg,#b02a2f,var(--book));box-shadow:2px 3px 6px rgba(0,0,0,.3)}
.strip{position:absolute;left:0;top:1140px;width:809px;height:60px;background:var(--strip);
  display:flex;align-items:center;justify-content:flex-end;padding-right:26px;font-size:13px;font-weight:500}
</style>
</head>
<body>
<div class="card">
  <svg class="chart" width="809" height="1200" viewBox="0 0 809 1200" aria-hidden="true">
    <polygon points="0,900 130,860 240,800 330,830 430,700 520,640 600,560 680,470 760,380 809,340 809,1140 0,1140" fill="rgba(255,255,255,0.22)"/>
    <polyline points="0,900 130,860 240,800 330,830 430,700 520,640 600,560 680,470 760,380 809,340" fill="none" stroke="rgba(255,255,255,0.75)" stroke-width="3"/>
  </svg>

  <h1 class="v title first">残暑お見舞い</h1>
  <div class="v title second" aria-hidden="false">申し上げます</div>

  <div class="message">
    <p>コロナ禍と暑さで汗が噴き出るような日々が続きますが、</p>
    <p>いかがお過ごしでしょうか？</p>
    <p>汗はかけばかくほど、老廃物が体内から出て、</p>
    <p>心も体も健康になります。</p>
    <p>汗をかかないようにすることは、</p>
    <p>決して良いことではありません。</p>
    <p>会社にとっても、今年は汗（特別損失）を出せるチャンスです。</p>
    <p>個人も会社もたくさんの汗を出して、</p>
    <p>より健康体になられること、心より祈念申し上げます。</p>
  </div>

  <div class="v company">ノルフェン・パートナーズ</div>
  <div class="v name n1">松本　清志</div>
  <div class="v name n2">長谷　宗一郎</div>
  <div class="v name n3">柴田　昌平</div>

  <div class="city" role="img" aria-label="青空と白い雲の下に広がる都市のビル群の写真"></div>
  <div class="book" role="img" aria-label="新刊『伸びる会社へ組み直す』の書籍写真"></div>

  <div class="strip">松本清志の最新刊「伸びる会社へ組み直す」定価10,780円（税込）</div>
</div>
</body>
</html>
```